Website Design for Non-profit

We are looking for a new site design for the Patrons of the Northern Heritage Hall. The current site can be found at
http://www.patrons-hall.org/pnhhindex_e.html
The URL is provided for reference. We want a completely different look and layout which is shown in the specifications document. Visiting the site, you can learn more about the organization.
Initially, we would like a home page, and inside page provided. Once we a home page and inside page are selected, we would like a simple mobile template provided.
I have attached a full description of the project as well as the specifications document and a zip file containing images for the site.
As mentioned in the specs document, we want to include an image of the museum in the header. The zip file is too large for us to upload (80 meg). The zip file can be obtained by clicking this link:
http://qzl.cc/TrWpKe
The zip file contains several exterior photos and you can select the one you feel is most appropriate to your design.
Reason: A long weekend is coming up and a few members of the team are unavailable for review.
Reason: Reviewing designs. Should have a decision next week.
Reason: We are discussing the designs and looking to reach a consensus. I will be implementing some designs today or tomorrow. Hopefully final selection will be next week.
Reason: Still reviewing designs. Hope to get a decision soon.
Reason: Working to finalize the design. Very close.
Industry/Entity Type
Museum
Look and feel
Each slider illustrates characteristics of the customer's brand and the style your logo design should communicate.

```html
<!DOCTYPE html>
<html lang="en">
<head>
<meta charset="utf-8">
<title>Patrons of the Northern Heritage Hall</title>
<link href="https://fonts.googleapis.com/css2?family=Roboto:wght@400;500&display=swap" rel="stylesheet">
<style>
:root{
  --dark:#2a2a2a;
  --olive:#9c8a3b;
  --red:#c4161c;
  --red-dark:#9e1015;
  --blue:#1ea1cf;
  --text:#444;
  --muted:#555;
  --line:#dcdcdc;
  --panel:#fff;
  --bg:#efefef;
}
*{box-sizing:border-box;margin:0;padding:0}
html,body{width:1029px;height:1200px;overflow:hidden}
body{font-family:'Roboto',Arial,sans-serif;color:var(--text);position:relative;
  background:repeating-linear-gradient(135deg,#f3f3f3 0 2px,#ececec 2px 4px)}
.abs{position:absolute}
/* top bar */
.topbar{left:0;top:0;width:1029px;height:27px;background:var(--dark)}
.social{top:3px;width:19px;height:19px;border-radius:2px}
.social.one{left:106px;background:#3b5a9a}
.social.two{left:133px;background:#2aa9e0}
.toplinks{left:179px;top:8px;display:flex;gap:26px;font-size:9.5px;color:#bbb;letter-spacing:.3px}
.toplinks small{font-size:6px}
.fontsize{left:703px;top:6px;display:flex;gap:12px;font-size:11px;font-weight:500;color:#fff}
.search{left:780px;top:4px;width:146px;height:20px;background:#fff;border-radius:2px}
.search svg{position:absolute;right:8px;top:5px}
/* header */
.header{left:0;top:27px;width:1029px;height:108px;background:linear-gradient(#fff,#eee)}
.brand{left:103px;top:55px;display:flex;align-items:center;gap:10px;font-size:22px;font-weight:500;color:#333;letter-spacing:6px}
.brand i{width:16px;height:16px;background:var(--olive);display:block}
.brand-sub{left:103px;top:86px;font-size:11px;color:#666;letter-spacing:1px}
/* hero */
.band{left:0;top:135px;width:1029px;height:330px;background:var(--olive)}
.hero{left:103px;top:135px;width:823px;height:270px;background:linear-gradient(90deg,#6b5a36,#8a7a55 35%,#5d5545 65%,#3d3530)}
.dots{left:468px;top:374px;display:flex;gap:6px}
.dots span{width:9px;height:9px;border-radius:50%;border:1.5px solid #ccc}
.dots span.on{background:#f28c28;border-color:#fff}
.nav{left:103px;top:405px;width:823px;height:42px;background:linear-gradient(#d21c22,#b3131a);display:flex;justify-content:space-between;align-items:center;padding:0 9px;font-size:12.5px;font-weight:500;color:#fff;border-bottom:2px solid var(--red-dark)}
/* tabs */
.tab{top:481px;height:31px;border-radius:5px 5px 0 0;font-size:12px;display:flex;align-items:center;padding:0 10px}
.tab.active{left:103px;width:97px;background:#fff;border:1px solid var(--line);border-bottom:none;color:#555;height:32px;z-index:2}
.tab.blue{background:var(--blue);color:#fff;border-bottom:2px solid #1483aa}
.intro{left:103px;top:511px;width:823px;height:114px;background:#fff;border:1px solid var(--line)}
.intro .photo{position:absolute;left:8px;top:10px;width:203px;height:93px;background:linear-gradient(90deg,#b59363,#8a6f4e 50%,#c09a6a)}
.intro p{position:absolute;left:229px;width:584px;font-size:13.3px;line-height:15.5px;color:#555;text-align:justify}
/* panels */
.panel{background:#fff;border:1px solid var(--line);border-radius:6px}
.panel-head{height:36px;border-bottom:1px solid var(--line);display:flex;justify-content:space-between;align-items:center;padding:0 9px 0 7px;font-size:12px;color:#444;letter-spacing:.2px}
.panel-head a{color:var(--red);font-size:10.5px;font-weight:500;text-decoration:none}
.item{position:relative;height:98px;margin:0 5px;border-bottom:1px solid var(--line)}
.item:last-child{border:none}
.thumb{position:absolute;left:1px;top:8px;width:74px;height:74px}
.item .body{position:absolute;left:91px;top:7px;width:488px;font-size:9.6px;line-height:16.3px;color:var(--muted)}
.item h3{font-weight:400;font-size:11px;color:var(--red);line-height:16px}
/* side */
.tile{width:206px;height:131px;border-radius:6px;overflow:hidden}
.tile .label{position:absolute;left:0;bottom:21px;height:32px;padding:0 20px 0 11px;background:var(--red);color:#fff;font-size:12.3px;font-weight:500;display:flex;align-items:center;clip-path:polygon(0 0,92% 0,100% 100%,0 100%)}
.bureau{left:720px;top:931px;width:206px;height:164px;background:#fff;border:1px solid var(--line);border-radius:6px 6px 0 0}
.bureau .head{height:30px;background:linear-gradient(#b2a04c,var(--olive));color:#fff;font-size:12.2px;font-weight:500;display:flex;align-items:center;padding-left:8px;border-radius:6px 6px 0 0}
.bureau p{font-size:9.6px;line-height:14.5px;color:var(--muted);text-align:justify;padding:0 4px 0 4px;margin-top:8px}
.bureau a{display:block;font-size:9.8px;color:var(--blue);padding:6px 4px 0;text-decoration:none}
/* footer */
.footlinks{left:103px;top:1132px;display:flex;gap:17px;font-size:9.4px;color:#666}
.badge{top:1116px;height:44px;background:#fff;border:1px solid #e2e2e2}
.bottombar{left:0;top:1170px;width:1029px;height:30px;background:var(--dark);color:#ddd;font-size:10px}
.bottombar span{position:absolute;top:9px}
</style>
</head>
<body>
<div class="abs topbar"></div>
<span class="abs social one" role="img" aria-label="Social network link"></span>
<span class="abs social two" role="img" aria-label="Social network link"></span>
<nav class="abs toplinks"><span>CONTACT</span><span>RELATED SITES</span><span>DONATE</span><span>SITEMAP</span><span>FRANÇAIS</span><span>MEMBER LOGIN <small>(NOT A MEMBER?)</small></span></nav>
<div class="abs fontsize"><span>A-</span><span>A</span><span>A+</span></div>
<div class="abs search"><svg width="8" height="8" viewBox="0 0 8 8"><circle cx="3" cy="3" r="2.2" fill="none" stroke="#777" stroke-width="1"/><line x1="4.6" y1="4.6" x2="7.5" y2="7.5" stroke="#777" stroke-width="1.2"/></svg></div>

<header class="abs header"></header>
<div class="abs brand"><i></i>PNHH</div>
<div class="abs brand-sub">Patrons of the Northern Heritage Hall</div>

<div class="abs band"></div>
<div class="abs hero" role="img" aria-label="Visitors viewing a gallery of framed wartime paintings"></div>
<div class="abs dots"><span></span><span class="on"></span><span></span><span></span></div>
<nav class="abs nav"><span>HOME</span><span>ABOUT</span><span>SUPPORT PNHH</span><span>EVENTS</span><span>PROJECTS &amp; PROGRAMS</span><span>MEET THE PATRONS</span><span>VOLUNTEERS</span><span>PUBLICATIONS</span></nav>

<div class="abs tab active">BE A FRIEND</div>
<div class="abs tab blue" style="left:207px;width:96px">BE A DONOR</div>
<div class="abs tab blue" style="left:315px;width:121px">BE A VOLUNTEER</div>
<section class="abs intro">
  <div class="photo" role="img" aria-label="Three smiling members of the patrons group"></div>
  <p style="top:10px">You are invited to become a friend Help us help the Northern Heritage Hall to support the Hall in its mission to educate, preserve and commemorate Canada’s military history.</p>
  <p style="top:71px">The patrons fulfill our mandate by raising funds for acquisitions and programs, providing volunteers in the galleries and conducting special events at the Hall</p>
</section>

<section class="abs panel" style="left:103px;top:641px;width:591px;height:226px">
  <div class="panel-head">LATEST EVENTS<a href="#">MORE</a></div>
  <div class="item"><div class="thumb" role="img" aria-label="Submarine at sea" style="background:linear-gradient(#8fb3d6,#2f4f6e 60%,#222)"></div>
    <div class="body"><h3>Lorem ipsum dolor sit amet, consectetur adipisicing elit,</h3>July 30,2013<br>Ut enim ad minim veniam, quis nostrud exercitation ullamco laboris nisi ut aliquip ex ea commodo consequat. Duis aute irure dolor in reprehenderit in voluptate velit esse cillum dolore eu fugiat nulla pariatur. Excepteur sint occaecat cupidatat non proident, sunt in culpa qui officia deserunt mollit anim id est laborum</div></div>
  <div class="item"><div class="thumb" role="img" aria-label="Black and white photo of a warship" style="background:linear-gradient(#d8d8d8,#777)"></div>
    <div class="body"><h3>Lorem ipsum dolor sit amet, consectetur adipisicing elit,</h3>July 30,2013<br>Ut enim ad minim veniam, quis nostrud exercitation ullamco laboris nisi ut aliquip ex ea commodo consequat. Duis aute irure dolor in reprehenderit in voluptate velit esse cillum dolore eu fugiat nulla pariatur. Excepteur sint occaecat cupidatat non proident, sunt in culpa qui officia deserunt mollit anim id est laborum</div></div>
</section>

<section class="abs panel" style="left:103px;top:875px;width:591px;height:220px">
  <div class="panel-head">ANNOUNCEMENTS<a href="#">MORE</a></div>
  <div class="item" style="height:92px"><div class="thumb" role="img" aria-label="Veterans at a ceremony" style="background:linear-gradient(#c9cfd6,#5a4c4c)"></div>
    <div class="body"><h3>Lorem ipsum dolor sit amet, consectetur adipisicing elit,</h3>July 30,2013<br>Ut enim ad minim veniam, quis nostrud exercitation ullamco laboris nisi ut aliquip ex ea commodo consequat. Duis aute irure dolor in reprehenderit in voluptate velit esse cillum dolore eu fugiat nulla pariatur. Excepteur sint occaecat cupidatat non proident, sunt in culpa qui officia deserunt mollit anim id est laborum</div></div>
  <div class="item"><div class="thumb" role="img" aria-label="Vintage bomber aircraft in flight" style="background:linear-gradient(#7d9a8a,#3f5a50)"></div>
    <div class="body"><h3>Lorem ipsum dolor sit amet, consectetur adipisicing elit,</h3>July 30,2013<br>Ut enim ad minim veniam, quis nostrud exercitation ullamco laboris nisi ut aliquip ex ea commodo consequat. Duis aute irure dolor in reprehenderit in voluptate velit esse cillum dolore eu fugiat nulla pariatur. Excepteur sint occaecat cupidatat non proident, sunt in culpa qui officia deserunt mollit anim id est laborum</div></div>
</section>

<div class="abs tile" style="left:720px;top:641px;background:linear-gradient(#3b3e3a,#6c6e5a 60%,#4a4a40)" role="img" aria-label="Tank on display in a museum hall"><span class="label">PHOTO GALLERY</span></div>
<div class="abs tile" style="left:720px;top:786px;background:linear-gradient(90deg,#6a4a3a,#8a2c2c 40%,#4f4a5a 70%,#6a5030)" role="img" aria-label="Row of service medals and ribbons"><span class="label">MEMBER TREASURES</span></div>

<aside class="abs bureau">
  <div class="head">SPEAKER’S BUREAU</div>
  <p>Lorem ipsum dolor sit amet, consectetur adipisicing elit, sed do eiusmod tempor incididunt ut labore et dolore magna aliqua.</p>
  <p>Ut enim ad minim veniam, Ut enim ad minim veniam, quis nostrud exercitation ullamco laboris nisi ut aliquip</p>
  <a href="#">Read More</a>
</aside>

<nav class="abs footlinks"><span>Home</span><span>About</span><span>Support PNHH</span><span>Events</span><span>Projects &amp; Programs</span><span>Meet the Patrons</span><span>Volunteers</span><span>Publications</span></nav>
<div class="abs badge" style="left:709px;width:53px" role="img" aria-label="Partner badge"></div>
<div class="abs badge" style="left:774px;width:152px" role="img" aria-label="Partner badge"></div>

<footer class="abs bottombar">
  <span style="left:104px">Copyright 2013 Patrons of the Northern Heritage Hall. All Rights Reserved.</span>
  <span style="right:103px">12 Harbour Lane, Kingsford, Ontario K0A 2B4</span>
</footer>
</body>
</html>
```